tall cedar health and wellness group.

need a full website design , all information provided in word document labeled website blue print
Updates

Need extra days to review

Target Market(s)

first responders, military , people in crisis

Coding

Coded - Design and coding required

Number of Pages Required

1 page

```html
<!DOCTYPE html>
<html lang="en">
<head>
<meta charset="utf-8">
<title>Tall Cedar Health &amp; Wellness Group</title>
<link href="https://fonts.googleapis.com/css2?family=Montserrat:wght@400;500;600;700;800&display=swap" rel="stylesheet">
<style>
:root{
  --navy:#1f3f73;
  --orange:#f7720f;
  --grey:#e0e0e0;
  --card-grey:#8a8a8a;
  --ink:#2a2a2a;
  --muted:#555;
  --footer:#262626;
  --white:#fff;
}
*{box-sizing:border-box;margin:0;padding:0}
html,body{width:1200px;height:4556px;overflow:hidden}
body{font-family:"Montserrat",sans-serif;color:var(--ink);background:var(--white)}
.page{position:relative;width:1200px;height:4556px;overflow:hidden}
.abs{position:absolute}
.btn{position:absolute;display:flex;align-items:center;justify-content:center;border-radius:26px;font-size:13px;font-weight:700;letter-spacing:.5px;text-transform:uppercase;color:var(--white);background:var(--orange)}
.btn-outline{background:transparent;border:2px solid var(--white)}
/* header & hero */
.hero{position:absolute;left:0;top:0;width:1200px;height:760px;background:linear-gradient(100deg,#6e6158 0%,#8b7a69 35%,#b49a74 65%,#a88a55 100%)}
.hero-shade{position:absolute;inset:0;background:linear-gradient(90deg,rgba(20,20,25,.55) 0%,rgba(20,20,25,.25) 55%,rgba(0,0,0,0) 100%)}
.nav{position:absolute;top:68px;font-size:13px;font-weight:700;color:var(--white);letter-spacing:.3px}
.nav.active{text-decoration:underline;text-underline-offset:5px}
.brand{position:absolute;left:522px;top:40px;width:156px;text-align:center;color:var(--white)}
.brand-mark{width:34px;height:34px;border-radius:50%;background:var(--white);margin:0 auto 8px}
.brand-name{font-size:17px;font-weight:700;letter-spacing:.5px}
.brand-sub{font-size:7px;font-weight:600;letter-spacing:.6px;text-transform:uppercase}
.hero-title{position:absolute;left:74px;top:260px;font-size:45px;line-height:48px;font-weight:800;color:var(--white);letter-spacing:1px}
.hero-text{position:absolute;left:74px;top:410px;width:620px;font-size:20px;line-height:31px;font-weight:600;color:var(--white)}
/* headings */
.section-title{position:absolute;left:0;width:1200px;text-align:center;font-size:34px;font-weight:700;letter-spacing:.5px;color:var(--ink)}
.section-title .accent{color:var(--navy)}
.tilde{position:absolute}
.body-copy{font-size:14px;line-height:25px;color:#333;text-align:center}
/* about */
.about-photo{position:absolute;left:74px;top:848px;width:424px;height:424px;border-radius:6px;background:linear-gradient(135deg,#c9ced3 0%,#e3d4c4 50%,#8f9aa6 100%)}
/* service cards */
.service-card{position:absolute;top:1608px;width:242px;height:268px;border-radius:6px;overflow:hidden}
.service-card .label{position:absolute;left:0;bottom:0;width:100%;height:76px;background:linear-gradient(0deg,rgba(0,0,0,.8),rgba(0,0,0,0));padding:18px 14px 0;font-size:13px;line-height:19px;font-weight:700;color:var(--white);text-transform:uppercase}
.service-card .go{position:absolute;right:14px;bottom:22px;width:18px;height:18px;border-radius:50%;background:var(--white)}
.service-card.is-active{outline:4px solid var(--navy);outline-offset:0}
.chev{position:absolute;top:1731px}
/* audience cards */
.audience-card{position:absolute;top:2894px;width:242px;height:287px;background:var(--white);border-radius:4px;text-align:center;padding-top:20px}
.audience-card svg{display:block;margin:0 auto}
.audience-card h3{margin-top:18px;font-size:16px;line-height:24px;font-weight:700;color:var(--navy);text-transform:uppercase}
.audience-card p{margin:10px auto 0;width:200px;font-size:13px;line-height:21px;color:#444}
.audience-card.is-active{background:var(--card-grey)}
.audience-card.is-active h3,.audience-card.is-active p{color:var(--white)}
.dots{position:absolute;display:flex;gap:8px}
.dots span{width:9px;height:9px;border-radius:50%;background:#bbb}
/* partners */
.partner{position:absolute;top:3527px;width:242px;height:92px;border:2px solid #dcdcdc;border-radius:4px;display:flex;align-items:center;justify-content:center;font-size:27px;font-weight:700;color:#8a8a8a}
/* CTA */
.cta{position:absolute;left:0;top:3742px;width:1200px;height:430px;background:linear-gradient(90deg,#1b3a6b,#2a4f86 50%,#1b3a6b)}
.cta-title{position:absolute;left:0;top:3808px;width:1200px;text-align:center;font-size:34px;line-height:40px;font-weight:700;color:var(--white);letter-spacing:1px}
.cta-text{position:absolute;left:0;top:3940px;width:1200px;text-align:center;font-size:21px;color:var(--white);letter-spacing:.5px}
/* footer */
.footer{position:absolute;left:0;top:4170px;width:1200px;height:386px;background:var(--footer);color:#ddd}
.foot-col{position:absolute;top:84px;font-size:13px;line-height:29px}
.foot-col h4{font-size:18px;font-weight:500;color:var(--white);margin-bottom:4px}
.foot-brand{position:absolute;left:86px;top:92px;width:220px;text-align:center}
.foot-brand .brand-mark{background:#9a9a9a}
.foot-brand .brand-name{color:var(--navy);font-size:20px}
.foot-brand .brand-sub{color:var(--navy)}
.foot-copy{margin-top:26px;font-size:11px;line-height:21px;color:#ddd}
.socials{display:flex;gap:16px;margin-top:18px}
.socials span{width:18px;height:18px;border-radius:50%;background:#ddd}
</style>
</head>
<body>
<div class="page">

  <!-- Hero -->
  <div class="hero" role="img" aria-label="Photo of a smiling woman in a yellow cardigan during a supportive group conversation"><div class="hero-shade"></div></div>
  <span class="nav active" style="left:74px">HOME</span>
  <span class="nav" style="left:163px">ABOUT US</span>
  <span class="nav" style="left:285px">SERVICES</span>
  <span class="nav" style="left:402px">OUR TEAM</span>
  <span class="nav" style="left:717px">JOIN OUR TEAM</span>
  <span class="nav" style="left:884px">FAQ</span>
  <span class="nav" style="left:957px">CONTACT US</span>
  <div class="brand">
    <div class="brand-mark"></div>
    <div class="brand-name">TALL CEDAR</div>
    <div class="brand-sub">Health &amp; Wellness Group</div>
  </div>
  <h1 class="hero-title">STRONGER MINDS.<br>HEALTHIER BODIES.<br>BETTER LIVES.</h1>
  <p class="hero-text">Holistic wellness programs built for the unique needs of frontline and public service workers.</p>
  <a class="btn" style="left:74px;top:500px;width:212px;height:50px">Join Our Team</a>
  <a class="btn btn-outline" style="left:297px;top:500px;width:245px;height:50px">Book an Appointment</a>

  <svg class="abs" style="left:0;top:680px" width="1200" height="110" viewBox="0 0 1200 110">
    <path d="M0 40 C300 110 800 130 1200 40 L1200 0 L0 0 Z" fill="#8e7b67" opacity="0"/>
    <path d="M0 0 L0 40 C260 20 420 60 620 78 C820 96 1000 60 1200 30 L1200 0 Z" fill="none"/>
    <path d="M0 60 C200 0 420 20 620 60 C820 100 1000 60 1200 20 L1200 110 L0 110 Z" fill="#fff"/>
    <path d="M115 38 C320 20 520 60 700 82 C850 100 960 84 1085 72 C960 92 840 108 690 96 C520 82 330 38 115 38 Z" fill="var(--navy)"/>
  </svg>

  <!-- About -->
  <div class="about-photo" role="img" aria-label="Photo of a smiling woman at a desk, framed in a leaf shape with a blue wave"></div>
  <h2 class="section-title" style="left:524px;width:600px;top:852px;font-size:34px;line-height:40px"><span class="accent">ABOUT TALL CEDAR</span><br>HEALTH WELLNESS GROUP</h2>
  <svg class="tilde" style="left:779px;top:946px" width="90" height="14" viewBox="0 0 90 14"><path d="M2 10 C30 0 60 2 88 10 C60 6 30 6 2 10Z" fill="var(--navy)" stroke="var(--navy)" stroke-width="3"/></svg>
  <div class="abs body-copy" style="left:540px;top:973px;width:568px">
    <p>Nemo enim ipsam voluptatem quia voluptas sit aspernatur aut odit aut fugit, sed quia consequuntur magni dolores eos qui ratione voluptatem sequi nesciunt. Neque porro quisquam est, qui dolorem ipsum quia dolor sit amet, consectetur, adipisci velit, sed quia non numquam eius modi tempora incidunt ut labore et dolore magnam aliquam.</p>
    <p style="margin-top:8px">Nemo enim ipsam voluptatem quia voluptas sit aspernatur aut odit aut fugit, sed quia consequuntur magni dolores eos qui ratione voluptatem sequi nesciunt. Neque porro quisquam est.</p>
  </div>
  <a class="btn" style="left:742px;top:1207px;width:166px;height:51px">Learn More</a>

  <!-- Services band -->
  <svg class="abs" style="left:0;top:1340px" width="1200" height="80" viewBox="0 0 1200 80">
    <path d="M0 60 C200 30 420 20 620 45 C820 70 1000 72 1200 50 L1200 80 L0 80 Z" fill="var(--grey)"/>
    <path d="M115 40 C300 10 520 14 700 36 C850 52 960 60 1085 76 C960 70 840 66 690 52 C520 36 330 26 115 40 Z" fill="var(--navy)"/>
  </svg>
  <div class="abs" style="left:0;top:1420px;width:1200px;height:640px;background:var(--grey)"></div>
  <h2 class="section-title" style="top:1494px"><span class="accent">OUR</span> SERVICES</h2>
  <svg class="tilde" style="left:555px;top:1550px" width="90" height="14" viewBox="0 0 90 14"><path d="M2 10 C30 0 60 2 88 10 C60 6 30 6 2 10Z" fill="var(--navy)" stroke="var(--navy)" stroke-width="3"/></svg>

  <svg class="chev" style="left:44px" width="18" height="24" viewBox="0 0 18 24"><path d="M13 3 L4 12 L13 21" fill="none" stroke="#333" stroke-width="2"/></svg>
  <svg class="chev" style="left:1138px" width="18" height="24" viewBox="0 0 18 24"><path d="M5 3 L14 12 L5 21" fill="none" stroke="#333" stroke-width="2"/></svg>

  <div class="service-card" style="left:74px;background:linear-gradient(160deg,#8d8f94,#cbbfb2 55%,#5e5a57)" role="img" aria-label="Photo of a thoughtful woman seated on a sofa"><div class="label">Mental Health<br>Therapy</div><span class="go"></span></div>
  <div class="service-card is-active" style="left:344px;background:linear-gradient(160deg,#6a6c70,#a8a29a 55%,#403d3b)" role="img" aria-label="Photo of a man comforting a distressed colleague"><div class="label">Trauma &amp; First<br>Responder Support</div><span class="go"></span></div>
  <div class="service-card" style="left:613px;background:linear-gradient(160deg,#f2a33a,#d6833f 50%,#5a3320)" role="img" aria-label="Photo of a woman relaxing in a warm salt therapy room"><div class="label">Salt<br>Therapy</div><span class="go"></span></div>
  <div class="service-card" style="left:883px;background:linear-gradient(160deg,#7a6456,#b59c85 50%,#3e332d)" role="img" aria-label="Photo of a sound bowl session with people lying on mats"><div class="label">Sound &amp; Vibration<br>Therapy</div><span class="go"></span></div>
  <a class="btn" style="left:493px;top:1935px;width:212px;height:49px">View All Services</a>

  <!-- Mission -->
  <svg class="abs" style="left:0;top:2040px" width="1200" height="80" viewBox="0 0 1200 80">
    <path d="M0 20 C200 10 420 0 620 25 C820 50 1000 52 1200 20 L1200 80 L0 80 Z" fill="#fff"/>
    <path d="M0 0 L1200 0 L1200 20 C1000 52 820 50 620 25 C420 0 200 10 0 20 Z" fill="var(--grey)"/>
    <path d="M115 22 C300 -4 520 0 700 22 C850 38 960 46 1085 60 C960 56 840 52 690 38 C520 22 330 12 115 22 Z" fill="var(--navy)"/>
  </svg>
  <h2 class="section-title" style="left:73px;width:600px;top:2178px"><span class="accent">MISSION</span> &amp; VISION</h2>
  <svg class="tilde" style="left:328px;top:2230px" width="90" height="14" viewBox="0 0 90 14"><path d="M2 10 C30 0 60 2 88 10 C60 6 30 6 2 10Z" fill="var(--navy)" stroke="var(--navy)" stroke-width="3"/></svg>
  <div class="abs body-copy" style="left:90px;top:2268px;width:570px">
    <p>Nemo enim ipsam voluptatem quia voluptas sit aspernatur aut odit aut fugit, sed quia consequuntur magni dolores eos qui ratione voluptatem sequi nesciunt. Neque porro quisquam est, qui dolorem ipsum quia dolor sit amet, consectetur, adipisci velit, sed quia non numquam eius modi tempora incidunt ut labore et dolore magnam aliquam.</p>
    <p style="margin-top:14px">Nemo enim ipsam voluptatem quia voluptas sit aspernatur aut odit aut fugit, sed quia consequuntur magni dolores eos qui ratione voluptatem sequi nesciunt. Neque porro quisquam est, qui dolorem ipsum quia dolor sit amet, consectetur, adipisci velit, sed quia non numquam eius modi tempora incidunt ut labore et dolore magnam aliquam.</p>
  </div>
  <div class="abs" style="left:829px;top:2184px;width:296px;height:296px;border-radius:50%;background:radial-gradient(circle at 40% 35%,#ffd27a,#f08a3a 45%,#7b2d3a 100%)" role="img" aria-label="Photo of a woman with arms raised at sunset"></div>
  <div class="abs" style="left:703px;top:2333px;width:194px;height:194px;border-radius:50%;border:6px solid #fff;background:radial-gradient(circle at 50% 40%,#d8c2b0,#8ea39f 50%,#3e5e63 100%)" role="img" aria-label="Illustration of a brain growing like a flowering tree"></div>

  <!-- Who we serve -->
  <svg class="abs" style="left:0;top:2590px" width="1200" height="70" viewBox="0 0 1200 70">
    <path d="M0 60 C200 30 420 20 620 40 C820 60 1000 62 1200 50 L1200 70 L0 70 Z" fill="var(--grey)"/>
    <path d="M115 30 C300 4 520 8 700 26 C850 40 960 48 1085 64 C960 60 840 56 690 42 C520 28 330 18 115 30 Z" fill="var(--navy)"/>
  </svg>
  <div class="abs" style="left:0;top:2658px;width:1200px;height:650px;background:var(--grey)"></div>
  <h2 class="section-title" style="top:2748px"><span class="accent">WHO WE</span> SERVE</h2>
  <svg class="tilde" style="left:555px;top:2804px" width="90" height="14" viewBox="0 0 90 14"><path d="M2 10 C30 0 60 2 88 10 C60 6 30 6 2 10Z" fill="var(--navy)" stroke="var(--navy)" stroke-width="3"/></svg>
  <p class="abs" style="left:0;top:2844px;width:1200px;text-align:center;font-size:14px;color:#333">At Tall Cedar Health &amp; Wellness Group, we proudly support those who dedicate their lives to service, safety, and community care.</p>

  <div class="audience-card" style="left:74px">
    <svg width="80" height="70" viewBox="0 0 80 70" fill="none" stroke="#222" stroke-width="2.5"><path d="M8 22 L40 6 L72 22 Z"/><path d="M10 26 H70"/><path d="M18 30 V56 M31 30 V56 M49 30 V56 M62 30 V56"/><path d="M8 60 H72 M4 66 H76"/></svg>
    <h3>Law Enforcement<br>Personnel</h3>
    <p>Specialized support for officers, detectives, and public safety teams facing demanding schedules.</p>
  </div>
  <div class="audience-card is-active" style="left:344px">
    <svg width="80" height="70" viewBox="0 0 80 70" fill="none" stroke="#fff" stroke-width="2.5"><path d="M24 26 C24 10 56 10 56 26 Z"/><path d="M20 28 H60"/><circle cx="40" cy="36" r="9"/><path d="M18 68 V58 C18 50 28 46 40 46 C52 46 62 50 62 58 V68"/><path d="M30 56 H50 M30 62 H50"/></svg>
    <h3>Firefighters &amp; First<br>Responders</h3>
    <p>Specialized support for officers, detectives, and public safety teams facing demanding schedules.</p>
  </div>
  <div class="audience-card" style="left:613px">
    <svg width="80" height="70" viewBox="0 0 80 70" fill="none" stroke="#222" stroke-width="2.5"><circle cx="42" cy="20" r="12"/><path d="M20 68 V56 C20 46 30 40 42 40 C54 40 64 46 64 56 V68"/><path d="M36 40 V52 M48 40 V56 A4 4 0 1 1 47.9 56"/><path d="M12 18 H22 M17 13 V23"/></svg>
    <h3>Healthcare<br>Providers</h3>
    <p>Specialized support for officers, detectives, and public safety teams facing demanding schedules.</p>
  </div>
  <div class="audience-card" style="left:883px">
    <svg width="80" height="70" viewBox="0 0 80 70" fill="none" stroke="#222" stroke-width="2.5"><path d="M24 18 C24 6 56 6 56 18 Z"/><path d="M22 20 H58"/><circle cx="40" cy="30" r="9"/><path d="M18 68 V58 C18 48 28 44 40 44 C52 44 62 48 62 58 V68"/><path d="M40 44 V68 M30 56 H36"/></svg>
    <h3>Military<br>&amp; Veterans</h3>
    <p>Specialized support for officers, detectives, and public safety teams facing demanding schedules.</p>
  </div>
  <div class="dots" style="left:572px;top:3226px"><span style="background:var(--navy)"></span><span style="background:#333"></span><span style="background:#333"></span><span style="background:#333"></span></div>

  <!-- Community partners -->
  <svg class="abs" style="left:0;top:3290px" width="1200" height="80" viewBox="0 0 1200 80">
    <path d="M0 20 C200 10 420 0 620 25 C820 50 1000 52 1200 20 L1200 80 L0 80 Z" fill="#fff"/>
    <path d="M0 0 L1200 0 L1200 20 C1000 52 820 50 620 25 C420 0 200 10 0 20 Z" fill="var(--grey)"/>
    <path d="M115 22 C300 -4 520 0 700 22 C850 38 960 46 1085 60 C960 56 840 52 690 38 C520 22 330 12 115 22 Z" fill="var(--navy)"/>
  </svg>
  <h2 class="section-title" style="top:3424px"><span class="accent">COMMUNITY</span> PARTNERS</h2>
  <svg class="tilde" style="left:555px;top:3480px" width="90" height="14" viewBox="0 0 90 14"><path d="M2 10 C30 0 60 2 88 10 C60 6 30 6 2 10Z" fill="var(--navy)" stroke="var(--navy)" stroke-width="3"/></svg>
  <div class="partner" style="left:74px;color:var(--navy)">Northpoint</div>
  <div class="partner" style="left:344px">Vantara</div>
  <div class="partner" style="left:613px">Brightwell</div>
  <div class="partner" style="left:883px;font-size:22px">Oakridge Capital</div>
  <div class="dots" style="left:562px;top:3669px"><span style="background:var(--navy)"></span><span></span><span></span><span></span></div>

  <!-- CTA -->
  <div class="cta" role="img" aria-label="Photo of a group support circle under a deep blue overlay"></div>
  <h2 class="cta-title">READY TO PRIORITIZE YOUR HEALTH<br>AND WELL-BEING?</h2>
  <svg class="tilde" style="left:555px;top:3900px" width="90" height="14" viewBox="0 0 90 14"><path d="M2 10 C30 0 60 2 88 10 C60 6 30 6 2 10Z" fill="#fff" stroke="#fff" stroke-width="3"/></svg>
  <p class="cta-text">Take the first step toward a stronger, healthier, more resilient you.</p>
  <a class="btn" style="left:468px;top:3997px;width:262px;height:51px">Join Our Team</a>

  <!-- Footer -->
  <div class="footer">
    <svg class="abs" style="left:0;top:-30px" width="1200" height="50" viewBox="0 0 1200 50">
      <path d="M0 34 C300 10 800 10 1200 26 L1200 50 L0 50 Z" fill="#8a8a8a"/>
      <path d="M0 40 C300 18 800 18 1200 32 L1200 50 L0 50 Z" fill="var(--footer)"/>
    </svg>
    <div class="foot-brand">
      <div class="brand-mark"></div>
      <div class="brand-name">TALL CEDAR</div>
      <div class="brand-sub">Health &amp; Wellness Group</div>
      <p class="foot-copy">Copyright 2025 © Tall Cedar<br>All Right Reserved</p>
    </div>
    <div class="foot-col" style="left:353px">
      <h4>Quick Links</h4>
      Home<br>About Us<br>Services<br>Our Team<br>Join Our Team<br>FAQ<br>Contact Us
    </div>
    <div class="foot-col" style="left:587px">
      <h4>SERVICES</h4>
      Mental Health Therapy<br>Trauma &amp; First Responder support<br>Salt Therapy<br>Sound &amp; Vibration Therapy<br>Red-Light Therapy<br>PEMF Therapy<br>Neurofeedback<br>OT &amp; Rehabilitation
    </div>
    <div class="foot-col" style="left:899px;width:260px">
      <h4>Contact Info</h4>
      <p style="line-height:23px">48 Harbor Lane, Suite 12,<br>Riverton 20415, United States</p>
      <p style="margin-top:8px">+1-555-014-2290</p>
      <p style="margin-top:6px">hello@tallcedarwellness.com</p>
      <div class="socials"><span></span><span></span><span></span><span></span><span></span></div>
    </div>
  </div>

</div>
</body>
</html>
```